property maintenance company covering all trades Plumbing,heating ,electrical building carpentry

business cards

Target Market(s)

DOMESTIC HOUSEHOLDS

Industry/Entity Type

Property Maintenance

Contact Information for Business Card

dorian Fellowes
07841 305918
Brightwell Property Maintenace

Font styles to use
Sans Serif

Colors
eda3c7
d2a4cc
b7a5cd

```html
<!DOCTYPE html>
<html lang="en">
<head>
<meta charset="utf-8">
<title>Brightwell Property Maintenace – Business Cards</title>
<link rel="stylesheet" href="https://fonts.googleapis.com/css2?family=Playfair+Display:ital,wght@0,600;0,700;1,400&family=Raleway:wght@400;500&display=swap">
<style>
  :root {
    --pink: #eda3c7;
    --orchid: #d2a4cc;
    --lavender: #b7a5cd;
    --band: #e2a6cb;
    --paper: #ffffff;
    --ink: #2a2a2e;
    --slate: #2b2b2d;
    --slate-deep: #1f1f21;
    --backdrop: #1b1b1c;
  }
  * { box-sizing: border-box; margin: 0; padding: 0; }
  html, body {
    width: 1200px;
    height: 873px;
    overflow: hidden;
    background: var(--backdrop);
  }
  .canvas {
    position: relative;
    width: 1200px;
    height: 873px;
  }
  .card {
    position: absolute;
    width: 525px;
    height: 300px;
    border-radius: 14px;
    overflow: hidden;
    box-shadow: 0 10px 30px rgba(0,0,0,0.5);
  }
  .card--front { left: 50px; top: 150px; background: var(--paper); }
  .card--back  { left: 625px; top: 423px; background: var(--slate); }

  .brand-title {
    font-family: "Playfair Display", Georgia, serif;
    font-weight: 700;
    font-size: 27px;
    color: var(--pink);
    text-align: center;
    letter-spacing: 0.2px;
    white-space: nowrap;
  }
  .brand-services {
    display: flex;
    align-items: center;
    justify-content: center;
    gap: 8px;
    font-family: "Raleway", Arial, sans-serif;
    font-size: 13px;
    white-space: nowrap;
  }
  .brand-services::before,
  .brand-services::after {
    content: "";
    width: 26px;
    height: 1.5px;
    background: var(--pink);
  }

  /* front */
  .front-head { position: absolute; left: 0; right: 0; top: 40px; }
  .front-head .brand-services { color: var(--lavender); margin-top: 6px; }
  .rule-pair {
    position: absolute; left: 0; right: 0; top: 118px;
    height: 8px;
    border-top: 2px solid var(--pink);
    border-bottom: 2px solid var(--pink);
  }
  .front-band {
    position: absolute; left: 0; right: 0; top: 132px; bottom: 0;
    background: linear-gradient(180deg, var(--band), var(--orchid));
  }
  .holder {
    position: absolute; right: 290px; top: 70px;
    text-align: right;
  }
  .holder-name {
    font-family: "Playfair Display", Georgia, serif;
    font-weight: 700;
    font-size: 17px;
    color: var(--ink);
  }
  .holder-role {
    font-family: "Playfair Display", Georgia, serif;
    font-style: italic;
    font-size: 12px;
    color: #c184b3;
    margin-top: 1px;
  }
  .divider {
    position: absolute; left: 258px; top: 22px;
    width: 2px; height: 88px;
    background: linear-gradient(180deg, transparent, var(--ink) 50%, transparent);
    transform: rotate(-12deg);
  }
  .contact {
    position: absolute; left: 290px; top: 40px;
    display: flex; align-items: center; gap: 10px;
    font-family: "Raleway", Arial, sans-serif;
    font-size: 13px;
    color: #fbe9f3;
    letter-spacing: 0.5px;
  }
  .contact svg { width: 16px; height: 16px; fill: var(--ink); }

  /* back */
  .back-texture {
    position: absolute; inset: 0;
    background: linear-gradient(135deg, #353537 0%, var(--slate) 45%, var(--slate-deep) 100%);
  }
  .back-head { position: absolute; left: 0; right: 0; top: 112px; }
  .back-head .brand-services { color: var(--lavender); margin-top: 8px; }
</style>
</head>
<body>
<main class="canvas">

  <section class="card card--front" aria-label="Business card front">
    <div class="front-head">
      <div class="brand-title">Brightwell Property Maintenace</div>
      <div class="brand-services">Plumbing, Heating ,Electrical Building Carpentry</div>
    </div>
    <div class="rule-pair"></div>
    <div class="front-band">
      <div class="holder">
        <div class="holder-name">Dorian Fellowes</div>
        <div class="holder-role">President</div>
      </div>
      <div class="divider"></div>
      <div class="contact">
        <svg viewBox="0 0 24 24" aria-hidden="true">
          <path d="M6.6 10.8a15.2 15.2 0 0 0 6.6 6.6l2.2-2.2a1 1 0 0 1 1-.25 11.4 11.4 0 0 0 3.6.57 1 1 0 0 1 1 1V20a1 1 0 0 1-1 1A17 17 0 0 1 3 4a1 1 0 0 1 1-1h3.5a1 1 0 0 1 1 1c0 1.25.2 2.45.57 3.6a1 1 0 0 1-.25 1z"/>
        </svg>
        <span>07841 305918</span>
      </div>
    </div>
  </section>

  <section class="card card--back" aria-label="Business card back">
    <div class="back-texture" role="img" aria-label="Dark charcoal low-poly faceted background pattern"></div>
    <div class="back-head">
      <div class="brand-title">Brightwell Property Maintenace</div>
      <div class="brand-services">Plumbing, Heating ,Electrical Building Carpentry</div>
    </div>
  </section>

</main>
</body>
</html>
```